Business Card Design Project

Need a business card designed for a horse racing/gambling centered company.
Company name is BrightQuill.com.au
Company colours are similar to those in the logo.
Something clean and modern , designer given liberty to be creative.
Incorporate the logo is preferred.
Single or Double Sided fine
Must include :
Name
Mobile Number
Email Address
Reason: Apologies, I have been traveling unexpectedly with business and just need the extra two days to reply and give feedback before making a decision.
Industry/Entity Type
Business

```html
<!DOCTYPE html>
<html lang="en">
<head>
<meta charset="utf-8">
<title>BrightQuill.com.au – Business Card</title>
<link href="https://fonts.googleapis.com/css2?family=Jost:wght@300;400;500&display=swap" rel="stylesheet">
<style>
  :root {
    --bg: #d9d9db;
    --charcoal: #4a4a4d;
    --charcoal-deep: #3a3a3d;
    --teal: #138b87;
    --teal-light: #1fa6a0;
    --paper: #f6f6f6;
    --ring: #e2e2e2;
    --ink: #2e2e30;
    --white: #ffffff;
  }
  * { box-sizing: border-box; margin: 0; padding: 0; }
  html, body { width: 1200px; height: 900px; overflow: hidden; }
  body {
    background: var(--bg);
    font-family: "Jost", sans-serif;
    position: relative;
  }
  .card {
    position: absolute;
    left: 250px;
    width: 700px;
    height: 400px;
    overflow: hidden;
    box-shadow: 0 6px 18px rgba(0,0,0,0.18);
  }
  /* Front */
  .card-front { top: 40px; background: var(--charcoal); }
  .front-mark {
    position: absolute; left: 0; right: 0; top: 110px;
    display: flex; align-items: center; justify-content: center; gap: 16px;
  }
  .mark-dot {
    width: 34px; height: 34px; border-radius: 50%; background: var(--teal);
  }
  .mark-name {
    font-size: 40px; font-weight: 400; color: var(--white); letter-spacing: 1px;
  }
  .front-url {
    position: absolute; left: 0; right: 0; top: 300px;
    text-align: center; color: var(--teal-light);
    font-size: 22px; font-weight: 300; letter-spacing: 2px;
  }
  .front-rule {
    position: absolute; left: 0; right: 0; bottom: 0; height: 5px;
    background: linear-gradient(90deg, var(--teal) 0 38%, var(--white) 38% 62%, var(--teal) 62% 100%);
  }
  /* Back */
  .card-back { top: 460px; background: var(--paper); }
  .back-shapes { position: absolute; inset: 0; }
  .back-mark {
    position: absolute; left: 370px; top: 135px; width: 200px;
    display: flex; flex-direction: column; align-items: center; gap: 10px;
  }
  .back-mark .mark-dot { width: 28px; height: 28px; }
  .back-mark .mark-name { font-size: 21px; color: var(--teal); }
  .contact { position: absolute; left: 48px; top: 120px; color: var(--ink); }
  .contact-name { font-size: 40px; font-weight: 300; line-height: 1; }
  .contact-role { font-size: 12px; letter-spacing: 1px; margin-top: 6px; }
  .contact-line { font-size: 19px; font-weight: 300; margin-top: 6px; }
  .contact-line:first-of-type { margin-top: 34px; }
  .footer {
    position: absolute; left: 0; right: 0; bottom: 0; height: 92px;
    display: flex;
  }
  .monogram {
    width: 140px; background: var(--charcoal-deep);
    color: var(--white); font-size: 52px; font-weight: 300;
    display: flex; align-items: center; justify-content: center;
    border-right: 6px solid var(--white);
  }
  .footer-text {
    flex: 1; background: var(--charcoal);
    border-top: 5px solid var(--teal);
    padding: 14px 0 0 26px;
  }
  .tagline { color: var(--white); font-size: 27px; font-weight: 300; line-height: 1.1; }
  .footer-url { color: var(--teal-light); font-size: 17px; font-weight: 300; letter-spacing: 1.5px; margin-top: 4px; }
</style>
</head>
<body>
  <section class="card card-front">
    <div class="front-mark">
      <span class="mark-dot"></span>
      <span class="mark-name">BrightQuill.com.au</span>
    </div>
    <p class="front-url">WWW.BRIGHTQUILL.COM.AU</p>
    <div class="front-rule"></div>
  </section>

  <section class="card card-back">
    <svg class="back-shapes" width="700" height="400" viewBox="0 0 700 400">
      <rect x="360" y="0" width="340" height="310" fill="var(--charcoal-deep)"/>
      <line x1="470" y1="212" x2="700" y2="212" stroke="#2a2a2c" stroke-width="2"/>
      <circle cx="470" cy="160" r="168" fill="var(--paper)" stroke="var(--ring)" stroke-width="14"/>
    </svg>
    <div class="back-mark">
      <span class="mark-dot"></span>
      <span class="mark-name">BrightQuill.com.au</span>
    </div>
    <div class="contact">
      <h1 class="contact-name">Liam Harcourt</h1>
      <p class="contact-role">OWNER</p>
      <p class="contact-line">P: 0400555182</p>
      <p class="contact-line">liam@brightquill.com.au</p>
    </div>
    <div class="footer">
      <div class="monogram">BQ</div>
      <div class="footer-text">
        <p class="tagline">Dedicated to catering to punters</p>
        <p class="footer-url">WWW.BRIGHTQUILL.COM.AU</p>
      </div>
    </div>
  </section>
</body>
</html>
```